Design business cards for Vantrelo

I am looking for a clean, crisp and professional business card design. A logo already exists with which to work, which is attached in various formats. The design needs to be print ready. A clear brief is attached - please read it carefully and ensure you can deliver what is required. Looking forward to awarding the prize to a great design and great designer!

```html
<!DOCTYPE html>
<html lang="en">
<head>
<meta charset="utf-8">
<title>Vantrelo Business Cards</title>
<link href="https://fonts.googleapis.com/css2?family=Lato:wght@400;700&family=Noto+Serif:wght@400&display=swap" rel="stylesheet">
<style>
  :root {
    --backdrop: #1aab94;
    --card: #ffffff;
    --ink: #2b2b2b;
    --ink-soft: #555555;
    --accent-red: #e0432f;
    --accent-orange: #f08a2c;
    --accent-amber: #f4a23a;
    --mark: #7a3b86;
  }
  * { margin: 0; padding: 0; box-sizing: border-box; }
  html, body {
    width: 1200px; height: 684px; overflow: hidden;
    background: var(--backdrop);
    font-family: "Lato", sans-serif;
    color: var(--ink);
  }
  .card {
    position: absolute;
    top: 197px;
    width: 439px; height: 252px;
    background: var(--card);
    overflow: hidden;
  }
  .card--front { left: 137px; }
  .card--back { left: 623px; }

  .side-tab {
    position: absolute;
    width: 25px;
    background: linear-gradient(160deg, var(--accent-amber), var(--accent-orange) 50%, var(--accent-red));
  }
  .side-tab--left { left: 0; border-radius: 0 7px 7px 0; }
  .side-tab--right { right: 0; border-radius: 7px 0 0 7px; }
  .card--front .side-tab { top: 87px; height: 77px; }
  .card--back .side-tab { top: 16px; height: 79px; }

  .tagline {
    position: absolute; top: 24px; left: 0; right: 0;
    text-align: center; font-size: 14px; letter-spacing: 0.3px; color: var(--ink);
  }
  .brand {
    position: absolute; top: 98px; left: 0; right: 0;
    display: flex; align-items: center; justify-content: center; gap: 16px;
  }
  .brand-dot {
    width: 54px; height: 54px; border-radius: 50%;
    background: var(--mark);
  }
  .brand-name {
    font-family: "Noto Serif", serif; font-weight: 400;
    font-size: 40px; color: var(--ink); letter-spacing: 0.5px;
  }
  .address {
    position: absolute; top: 216px; left: 0; right: 0;
    text-align: center; font-size: 11px; color: var(--ink);
  }

  .person { position: absolute; left: 44px; top: 33px; }
  .person-name { font-size: 17px; font-weight: 700; color: var(--ink); }
  .person-name .first { color: var(--accent-red); }
  .person-credentials { font-size: 12px; color: var(--ink-soft); margin-top: 4px; }
  .person-role { font-size: 12px; font-weight: 700; margin-top: 8px; }

  .brand-small {
    position: absolute; top: 14px; right: 26px;
    display: flex; align-items: center; gap: 7px;
  }
  .brand-small .brand-dot { width: 20px; height: 20px; }
  .brand-small .brand-name { font-size: 17px; letter-spacing: 0; }

  .contact {
    position: absolute; left: 46px; top: 115px;
    border-collapse: collapse; font-size: 12.5px; color: var(--ink);
  }
  .contact th { font-weight: 400; text-align: left; width: 58px; padding: 2px 0 3px; }
  .contact td { padding: 2px 0 3px; }

  .footer-band { position: absolute; left: 0; bottom: 0; width: 439px; height: 37px; }
  .website {
    position: absolute; right: 18px; bottom: 11px;
    font-size: 12.5px; font-weight: 700; color: #ffffff;
  }
</style>
</head>
<body>
  <section class="card card--front">
    <div class="side-tab side-tab--left"></div>
    <div class="side-tab side-tab--right"></div>
    <p class="tagline">design is the expression of intent</p>
    <div class="brand">
      <span class="brand-dot"></span>
      <span class="brand-name">Vantrelo</span>
    </div>
    <p class="address">42 Elmwood Avenue, Ringwood North Victoria 3134 Australia</p>
  </section>

  <section class="card card--back">
    <div class="side-tab side-tab--left"></div>
    <div class="brand-small">
      <span class="brand-dot"></span>
      <span class="brand-name">Vantrelo</span>
    </div>
    <div class="person">
      <p class="person-name"><span class="first">Daniel</span> Hartwell</p>
      <p class="person-credentials">BE(Hons) PhD MIEAust GAICD</p>
      <p class="person-role">Director, Principal Consultant</p>
    </div>
    <table class="contact">
      <tr><th>phone</th><td>+61 (0)400 555 217</td></tr>
      <tr><th>e-mail</th><td>dhartwell@vantrelo.com.au</td></tr>
      <tr><th>skype</th><td>dan.hartwell27</td></tr>
      <tr><th>linkedin</th><td>au.linkedin.com/in/dhartwell</td></tr>
    </table>
    <svg class="footer-band" viewBox="0 0 439 37" preserveAspectRatio="none">
      <defs>
        <linearGradient id="band-warm" x1="0" y1="0" x2="1" y2="0">
          <stop offset="0" stop-color="#f29a34"/>
          <stop offset="1" stop-color="#e86a2c"/>
        </linearGradient>
      </defs>
      <rect width="439" height="37" fill="#e0432f"/>
      <polygon points="0,0 150,0 205,37 0,37" fill="url(#band-warm)"/>
    </svg>
    <p class="website">www.vantrelo.com.au</p>
  </section>
</body>
</html>
```